LoftHarbor - Coworking website design

LoftHarbor is a new global coworking brand, growing fast and establishing stylish locations and communities that inspire innovation and collaboration all around the world.
The project includes a complete website design, focused on delivering the company’s values and messages, provide information to site visitors and to generate leads.

Please review the attached design brief, for more information.

Target Market(s)

Both men and women. Decision makers in:
Small & medium businesses in various fields, but mainly technology firms (Startups or established brands).
Global enterprises.
Dynamic “new generation” companies.
Press

Number of Pages Required

2 page

Requirements
Must have
• Project Scope & deliverables:
• Concept and design for :
• Home page
• Deliver the values mentioned above.
• Showcase the cities in which the company has locations in.
• Show customer testimonials.
• Provide an interface (form) for booking a tour and/or leaving contact details for more information (two alternatives)
• Coworking location page - Each location is in the coolest part of a different major city, and has its own address, set of amenities (kitchen, fast internet etc,), area information (public transportation accessibility, sites near by, bars and restaurants in walking distance) and pricing for private offices (based on number of people per office). Each location page must have an interface to book a location tour.
• Site Navigation (header & footer) - allow simple navigation between multiple city pages, location pages and homepage. Growth of up to 50 locations in 25 cities.
• The navigation should account for Navigation to additional pages (not commissioned in this project) such as:
• Locations
• Enterprise
• Special promotions
• Blog
• Contact us
• About us
• Note - the site should account for geolocation variable display, showing different content for different locations.
• Deliverables must include all editable graphic files (photoshop or similar), as follows:
• Home page - Desktop view (preferably both)
• Location page - Mobile web view (preferably both)
• Navigation - both options

```html
<!DOCTYPE html>
<html lang="en">
<head>
<meta charset="utf-8">
<title>LoftHarbor – Coworking</title>
<link href="https://fonts.googleapis.com/css2?family=Roboto:wght@300;400;500;700&display=swap" rel="stylesheet">
<style>
:root{
  --blue:#2f9be0;
  --blue-dark:#1f7fc4;
  --ink:#1e1e1e;
  --text:#555b63;
  --muted:#8b9096;
  --line:#e3e6ea;
  --pale-blue:#e9f0fb;
  --pale-grey:#f2f3f5;
  --navy:#2d4a8a;
  --red:#e2463a;
  --footer:#16191f;
  --white:#fff;
}
*{box-sizing:border-box;margin:0;padding:0}
html,body{width:1200px;height:4592px;overflow:hidden}
body{font-family:"Roboto",Arial,sans-serif;color:var(--text);background:var(--white);position:relative}
.abs{position:absolute}
.section{position:absolute;left:0;width:1200px}
.section-title{position:absolute;left:0;width:1200px;text-align:center;font-size:29px;font-weight:700;color:var(--ink);letter-spacing:.5px}
.btn-outline{position:absolute;height:42px;border:1px solid #cfe3f4;border-radius:21px;color:var(--blue);font-size:12px;font-weight:500;display:flex;align-items:center;justify-content:center;gap:8px;letter-spacing:.5px;background:var(--white)}
.btn-ghost{position:absolute;height:40px;border:2px solid rgba(255,255,255,.8);border-radius:20px;color:#fff;font-size:12px;font-weight:500;display:flex;align-items:center;justify-content:center;gap:8px;letter-spacing:.5px}
.arrow-dot{display:inline-block;width:13px;height:13px;border-radius:50%;background:currentColor;position:relative}
.arrow-dot::after{content:"";position:absolute;left:3px;top:4px;border-left:5px solid #fff;border-top:2.5px solid transparent;border-bottom:2.5px solid transparent}

/* Header */
.topline{top:0;height:4px;background:var(--blue)}
.header{top:4px;height:96px;background:var(--white)}
.brand{position:absolute;left:101px;top:28px;font-size:32px;font-weight:700;color:var(--ink);letter-spacing:-.5px}
.nav{position:absolute;left:425px;top:38px;display:flex;gap:36px;font-size:15px;color:#333}
.login{position:absolute;left:1031px;top:35px;width:70px;height:26px;border:1px solid var(--blue);border-radius:3px;color:var(--blue);font-size:12px;display:flex;align-items:center;justify-content:center}

/* Hero */
.hero{top:100px;height:476px;background:linear-gradient(135deg,#3a3f45 0%,#8c9097 35%,#c7c9cc 60%,#7e858e 100%)}
.hero-photo{position:absolute;inset:0;background:linear-gradient(90deg,rgba(40,44,50,.55),rgba(60,64,70,.25) 50%,rgba(40,44,50,.5))}
.hero-title{position:absolute;top:160px;left:0;width:1200px;text-align:center;color:#fff;font-size:40px;font-weight:700;letter-spacing:.5px}
.hero-sub{position:absolute;top:225px;left:0;width:1200px;text-align:center;color:#eef2f6;font-size:15px}
.field{position:absolute;top:277px;height:42px;background:#fff;border-radius:21px;font-size:13px;color:#666;display:flex;align-items:center;padding:0 22px;justify-content:space-between}
.field .caret{border-top:5px solid #777;border-left:4px solid transparent;border-right:4px solid transparent}
.start{position:absolute;left:842px;top:277px;width:122px;height:42px;border-radius:21px;background:var(--blue);color:#fff;font-size:14px;font-weight:700;display:flex;align-items:center;justify-content:center;gap:6px}
.slide-arrow{position:absolute;top:232px;color:#fff;font-size:18px}

/* About */
.about{top:576px;height:480px}
.about-photo{position:absolute;left:107px;top:82px;width:306px;height:306px;border-radius:50%;background:radial-gradient(circle at 45% 45%,#c9ccd0,#8d9297 70%,#6c7176)}
.about h2{position:absolute;left:444px;top:86px;font-size:27px;font-weight:700;color:var(--ink)}
.about p{position:absolute;left:444px;top:132px;width:640px;font-size:12.5px;line-height:24px;color:var(--muted)}

/* Locations */
.locations{top:1056px;height:642px;background:var(--pale-blue)}
.locations h2{position:absolute;left:101px;top:56px;font-size:29px;font-weight:700;color:var(--ink)}
.map{position:absolute;left:107px;top:122px;width:888px;height:459px;border-radius:40px;background:radial-gradient(ellipse at 50% 45%,#a9adb3,#c9ccd1 70%,rgba(201,204,209,0) 100%)}
.pin{position:absolute;width:36px;height:36px;border-radius:50%;background:var(--blue);color:#fff;font-size:13px;font-weight:700;display:flex;align-items:center;justify-content:center;border:3px solid #fff}

/* Testimonials */
.testimonials{top:1698px;height:462px}
.card{position:absolute;top:154px;width:318px;height:220px;border:1px solid var(--line);box-shadow:0 2px 6px rgba(0,0,0,.06);background:#fff}
.avatar{position:absolute;left:16px;top:20px;width:60px;height:60px;border-radius:50%;background:linear-gradient(#9aa3ad,#6d747d)}
.card .name{position:absolute;left:88px;top:26px;font-size:13px;color:var(--ink);font-weight:500}
.card .role{position:absolute;left:88px;top:46px;font-size:11px;color:var(--muted)}
.badge{position:absolute;right:16px;top:30px;height:26px;padding:0 12px;border-radius:3px;color:#fff;font-size:10px;font-weight:700;display:flex;align-items:center;gap:6px}
.badge i{width:9px;height:9px;background:#fff;display:block;border-radius:2px}
.card p{position:absolute;left:16px;top:96px;width:286px;font-size:11px;line-height:18px;color:var(--text)}
.card .meta{position:absolute;left:16px;top:188px;font-size:10.5px;color:var(--muted);display:flex;gap:14px}
.carousel-arrow{position:absolute;top:242px;width:44px;height:44px;border-radius:50%;border:1px solid #cfd3d8;color:#9aa0a7;display:flex;align-items:center;justify-content:center;font-size:16px}

/* Promo */
.promo{top:2160px;height:380px}
.promo-panel{position:absolute;top:0;height:380px;width:600px;color:#fff;text-align:center}
.enterprise{left:0;background:linear-gradient(135deg,#2b2e33,#4b4f55 50%,#2a2c30)}
.special{left:600px;background:linear-gradient(135deg,#3b8fd0,#2d80c6 60%,#2a76bb)}
.promo-panel h3{position:absolute;top:78px;left:0;width:600px;font-size:27px;font-weight:500;letter-spacing:.5px}
.promo-panel p{position:absolute;top:140px;left:100px;width:400px;font-size:12px;line-height:22px;color:rgba(255,255,255,.85)}

/* Values */
.values{top:2540px;height:404px}
.value{position:absolute;top:178px;width:200px;text-align:center}
.value svg{display:block;margin:0 auto}
.value span{display:block;margin-top:22px;font-size:15px;line-height:22px;color:var(--ink)}

/* Members */
.members{top:2944px;height:361px;background:var(--pale-grey)}
.logo-box{position:absolute;top:138px;height:107px;background:#fff;display:flex;align-items:center;justify-content:center;gap:8px;font-size:19px;font-weight:700;color:var(--ink)}
.logo-box i{display:block;width:14px;height:14px;background:var(--ink)}
.dots{position:absolute;top:276px;left:0;width:1200px;display:flex;justify-content:center;gap:8px}
.dots span{width:8px;height:8px;border-radius:50%;background:#c5c9ce}
.dots span:first-child{background:var(--blue)}

/* Blog */
.blog{top:3305px;height:872px}
.post-photo{position:absolute;width:496px;height:310px}
.post h4{position:absolute;font-size:16px;font-weight:700;color:var(--ink);letter-spacing:.2px}
.post p{position:absolute;width:460px;font-size:12px;line-height:24px;color:var(--muted)}

/* Footer */
.footer{top:4177px;height:415px;background:linear-gradient(180deg,#1c2028,#12151a)}
.footer h5{position:absolute;top:60px;font-size:16px;font-weight:500;color:#fff}
.contact-row{position:absolute;left:101px;display:flex;gap:16px;align-items:center;font-size:12px;line-height:18px;color:#c6cad0}
.contact-row .ic{width:30px;height:30px;border-radius:50%;background:#fff;flex:none;display:flex;align-items:center;justify-content:center}
.links{position:absolute;left:419px;top:104px;font-size:12px;line-height:31px;color:#c6cad0;list-style:none}
.newsletter p{position:absolute;left:594px;top:100px;font-size:12px;color:#c6cad0}
.email{position:absolute;left:594px;top:135px;width:376px;height:36px;background:#fff;font-size:12px;color:#888;padding:0 14px;display:flex;align-items:center}
.signup{position:absolute;left:979px;top:135px;width:120px;height:36px;background:var(--blue);color:#fff;font-size:14px;font-weight:700;display:flex;align-items:center;justify-content:center}
.social{position:absolute;left:594px;top:190px;display:flex;gap:8px}
.social span{width:28px;height:28px;border-radius:50%;background:var(--blue)}
.footer-rule{position:absolute;left:101px;top:330px;width:1000px;height:1px;background:#2f343c}
.copyright{position:absolute;left:0;top:366px;width:1200px;text-align:center;font-size:11px;color:#c6cad0}
</style>
</head>
<body>

<div class="section topline"></div>
<header class="section header">
  <div class="brand">LoftHarbor</div>
  <nav class="nav">
    <span>Locations</span><span>Enterprise</span><span>Special promotions</span><span>Blog</span><span>Contact us</span><span>About us</span>
  </nav>
  <div class="login">Log in</div>
</header>

<section class="section hero" role="img" aria-label="Photo of people working together at laptops in a coworking space">
  <div class="hero-photo"></div>
  <span class="slide-arrow" style="left:10px">&#8249;</span>
  <span class="slide-arrow" style="right:10px">&#8250;</span>
  <h1 class="hero-title">LoftHarbor Co-working</h1>
  <p class="hero-sub">Sed ut perspiciatis unde omnis iste natus error sit voluptatem accusantium doloremque laudan</p>
  <div class="field" style="left:236px;width:290px">Where you'd like space <span class="caret"></span></div>
  <div class="field" style="left:539px;width:290px">How many employees <span class="caret"></span></div>
  <div class="start">START <span>&#8250;</span></div>
</section>

<section class="section about">
  <div class="about-photo" role="img" aria-label="Round photo of hands typing on a laptop at a desk"></div>
  <h2>ABOUT COWORKING</h2>
  <p>Coworking is a style of work that involves a shared working environment. Unlike in a typical office environment, those coworking are usually employed by various organizations. Coworking is a gathering of a group of people who are working independently but who share values, and who are interested in the synergy that can happen from working with like-minded people. Coworking is not only about the physical place, but about establishing and being part of a community. LoftHarbor is focused on a stylish work environment that includes private offices, with shared lounges, meeting rooms and kitchens (and NOT a shared open space for freelancers).</p>
  <div class="btn-outline" style="left:444px;top:342px;width:159px">READ MORE <span class="arrow-dot"></span></div>
</section>

<section class="section locations">
  <h2>OUR LOCATIONS</h2>
  <div class="map" role="img" aria-label="World map showing city locations"></div>
  <div class="pin" style="left:304px;top:170px">9</div>
  <div class="pin" style="left:186px;top:212px">8</div>
  <div class="pin" style="left:536px;top:182px">11</div>
  <div class="pin" style="left:655px;top:140px">6</div>
  <div class="pin" style="left:970px;top:278px">5</div>
  <div class="pin" style="left:498px;top:302px">2</div>
  <div class="pin" style="left:618px;top:306px">1</div>
  <div class="pin" style="left:376px;top:342px">10</div>
  <div class="pin" style="left:537px;top:390px">3</div>
  <div class="pin" style="left:813px;top:438px">4</div>
  <div class="pin" style="left:185px;top:422px">7</div>
  <div class="pin" style="left:376px;top:548px">12</div>
</section>

<section class="section testimonials">
  <h2 class="section-title" style="top:82px">CUSTOMER TESTIMONIALS</h2>
  <div class="carousel-arrow" style="left:34px">&#8249;</div>
  <div class="carousel-arrow" style="left:1116px">&#8250;</div>

  <article class="card" style="left:101px">
    <div class="avatar" role="img" aria-label="Customer portrait"></div>
    <div class="name">Veritatis et</div><div class="role">quasi tourian</div>
    <div class="badge" style="background:var(--navy)"><i></i>FOLLOW</div>
    <p>Lorem ipsum dolor sit amet, consectetur adipiscing elit, sed do eiusmod tempor incididunt ut labore et dolore magna aliqua enim ad minim ut laborene</p>
    <div class="meta"><span>&#9825; Like</span><span>&#8618; Share</span><span>&#9633; Comments</span></div>
  </article>

  <article class="card" style="left:444px">
    <div class="avatar" role="img" aria-label="Customer portrait"></div>
    <div class="name">Veritatis et</div><div class="role">quasi tourian</div>
    <div class="badge" style="background:var(--red)"><i></i>FOLLOW</div>
    <p>Lorem ipsum dolor sit amet, consectetur adipiscing elit, sed do eiusmod tempor incididunt ut labore et dolore magna aliqua enim ad minim ut laborene</p>
    <div class="meta"><span>&#9825; Like</span><span>&#8618; Share</span><span>&#9633; Comments</span><span>13 hours ago</span></div>
  </article>

  <article class="card" style="left:783px">
    <div class="avatar" role="img" aria-label="Customer portrait"></div>
    <div class="name">Veritatis et</div><div class="role">quasi tourian</div>
    <div class="badge" style="background:var(--navy)"><i></i>FOLLOW</div>
    <p>Lorem ipsum dolor sit amet, consectetur adipiscing elit, sed do eiusmod tempor incididunt ut labore et dolore magna aliqua enim ad minim ut laborene</p>
    <div class="meta"><span>&#9825; Like</span><span>&#8618; Share</span><span>&#9633; Comments</span></div>
  </article>
</section>

<section class="section promo">
  <div class="promo-panel enterprise" role="img" aria-label="Dim photo of a team meeting in an office">
    <h3>ENTERPRISE</h3>
    <p>Sed ut perspiciatis unde omnis iste natus error sit voluptatem accusantium doloremque laudantium totam rem aperiam eaque ipsa quae ab illo inventore veritatis et quasi architecto beatae vitae dicta sunt explicabo</p>
    <div class="btn-ghost" style="left:238px;top:274px;width:126px">READ MORE <span class="arrow-dot"></span></div>
  </div>
  <div class="promo-panel special" role="img" aria-label="Blue tinted photo of people at a shared desk">
    <h3>SPECIAL PROMOTIONS</h3>
    <p>Sed ut perspiciatis unde omnis iste natus error sit voluptatem accusantium doloremque laudantium totam rem aperiam eaque ipsa quae ab illo inventore veritatis et quasi architecto beatae vitae dicta sunt explicabo</p>
    <div class="btn-ghost" style="left:238px;top:274px;width:126px">READ MORE <span class="arrow-dot"></span></div>
  </div>
</section>

<section class="section values">
  <h2 class="section-title" style="top:78px">VALUES TO DELIVER</h2>
  <div class="value" style="left:82px">
    <svg width="56" height="70" viewBox="0 0 56 70"><circle cx="28" cy="26" r="18" fill="#f6c23e"/><rect x="20" y="44" width="16" height="12" fill="#444"/><rect x="22" y="58" width="12" height="4" fill="#444"/></svg>
    <span>Inspire collaboration<br>&amp; Innovation</span>
  </div>
  <div class="value" style="left:292px">
    <svg width="64" height="70" viewBox="0 0 64 70"><circle cx="32" cy="34" r="28" fill="none" stroke="#4aa34a" stroke-width="3" stroke-dasharray="6 5"/><circle cx="22" cy="30" r="6" fill="#e9a23b"/><circle cx="42" cy="30" r="6" fill="#3b8ee0"/><rect x="14" y="40" width="16" height="10" rx="4" fill="#e9a23b"/><rect x="34" y="40" width="16" height="10" rx="4" fill="#3b8ee0"/></svg>
    <span>Idea sharing</span>
  </div>
  <div class="value" style="left:521px">
    <svg width="64" height="70" viewBox="0 0 64 70"><circle cx="32" cy="30" r="8" fill="#2f6fb5"/><rect x="20" y="42" width="24" height="14" rx="5" fill="#2f6fb5"/><path d="M32 4v10M12 14l6 6M52 14l-6 6" stroke="#e2463a" stroke-width="3"/><rect x="10" y="58" width="44" height="4" fill="#e2463a"/></svg>
    <span>Be a part of<br>an exclusive club</span>
  </div>
  <div class="value" style="left:714px">
    <svg width="64" height="70" viewBox="0 0 64 70"><circle cx="34" cy="22" r="12" fill="none" stroke="#e9853b" stroke-width="5" stroke-dasharray="5 3"/><circle cx="34" cy="22" r="4" fill="#e9853b"/><path d="M6 50h20l10 6h20v8H30L6 58z" fill="#3b8ee0"/></svg>
    <span>Realize<br>your greatness</span>
  </div>
  <div class="value" style="left:907px">
    <svg width="64" height="70" viewBox="0 0 64 70"><circle cx="22" cy="24" r="11" fill="none" stroke="#e2463a" stroke-width="5" stroke-dasharray="5 3"/><circle cx="44" cy="32" r="9" fill="none" stroke="#4aa34a" stroke-width="5" stroke-dasharray="4 3"/><circle cx="26" cy="50" r="9" fill="none" stroke="#e9a23b" stroke-width="5" stroke-dasharray="4 3"/></svg>
    <span>Style and<br>design awareness</span>
  </div>
</section>

<section class="section members">
  <h2 class="section-title" style="top:84px">OUR MEMBERS</h2>
  <div class="logo-box" style="left:107px;width:138px"><i></i>Quick Pear</div>
  <div class="logo-box" style="left:257px;width:144px"><i></i>Meadowline</div>
  <div class="logo-box" style="left:410px;width:141px">XYZ</div>
  <div class="logo-box" style="left:563px;width:266px;font-weight:400;font-size:26px;color:#444">Company LOGO</div>
  <div class="logo-box" style="left:845px;width:241px"><i></i>botly</div>
  <div class="dots"><span></span><span></span><span></span></div>
</section>

<section class="section blog">
  <h2 class="section-title" style="top:84px">BLOG POSTS</h2>
  <article class="post">
    <div class="post-photo" style="left:101px;top:162px;background:linear-gradient(135deg,#5d6165,#a9a39a 45%,#c8542f 70%,#6a6e72)" role="img" aria-label="Photo of an open-plan office with orange chairs"></div>
    <h4 style="left:637px;top:214px">ENTORE VERITATIS ET QUASI ARCHITECTO BEAT</h4>
    <p style="left:637px;top:248px">Sed ut perspiciatis unde omnis iste natus error sit voluptatem accusantium doloremque laudantium, totam rem aperiam, eaque ipsa quae ab illo inventore veritatis et quasi architecto beatae vitae dicta sunt explicabo. Nemo enim ipsam voluptatem, eaque ipsa quae ab illo quia voluptas sit aspernatur aut odit aut fugit.</p>
    <div class="btn-outline" style="left:637px;top:388px;width:136px">READ MORE <span class="arrow-dot"></span></div>
  </article>
  <article class="post">
    <h4 style="left:101px;top:518px">ILLO INVENTORE VERITATIS ET QUASI ARCHITECTO BEAT</h4>
    <p style="left:101px;top:552px">Sed ut perspiciatis unde omnis iste natus error sit voluptatem accusantium doloremque laudantium, totam rem aperiam, eaque ipsa quae ab illo inventore veritatis et quasi architecto beatae vitae dicta sunt explicabo. Nemo enim ipsam voluptatem, eaque ipsa quae ab illo quia voluptas sit aspernatur aut odit aut fugit.</p>
    <div class="btn-outline" style="left:101px;top:692px;width:136px">READ MORE <span class="arrow-dot"></span></div>
    <div class="post-photo" style="left:603px;top:475px;width:493px;background:linear-gradient(135deg,#2f6f86,#8fb4bd 45%,#d9c7a4 65%,#3d5560)" role="img" aria-label="Photo of a team giving a high five"></div>
  </article>
</section>

<footer class="section footer" role="contentinfo">
  <h5 style="left:101px">Contact Info</h5>
  <div class="contact-row" style="top:104px"><span class="ic"><svg width="12" height="14" viewBox="0 0 12 14"><path d="M6 0a5 5 0 0 0-5 5c0 4 5 9 5 9s5-5 5-9a5 5 0 0 0-5-5z" fill="#16191f"/></svg></span><span>58, sdis iatus error sit voluptatem<br>accusantium dolo</span></div>
  <div class="contact-row" style="top:156px"><span class="ic"><svg width="12" height="12" viewBox="0 0 12 12"><path d="M2 0l3 3-1.5 2a7 7 0 0 0 3.5 3.5L9 7l3 3-2 2C5 12 0 7 0 2z" fill="#16191f"/></svg></span><span>Phone : 555 010 4821</span></div>
  <div class="contact-row" style="top:204px"><span class="ic"><svg width="13" height="10" viewBox="0 0 13 10"><rect width="13" height="10" fill="#16191f"/><path d="M0 0l6.5 5L13 0" stroke="#fff" fill="none"/></svg></span><span>Email : info@loftharbor-mail.com</span></div>

  <h5 style="left:419px">Quick links</h5>
  <ul class="links"><li>Locations</li><li>Enterprise</li><li>Special promotions</li><li>Blog</li><li>Contact us</li><li>About us</li></ul>

  <div class="newsletter">
    <h5 style="left:594px">Subscribe Newsletter</h5>
    <p>Sed ut perspiciatis unde omnis iste natus error sit voluptatem accusantium</p>
    <div class="email">Email Address</div>
    <div class="signup">SIGN UP</div>
    <div class="social"><span></span><span></span><span></span><span></span><span></span></div>
  </div>

  <div class="footer-rule"></div>
  <div class="copyright">Copyrights © 2017. LoftHarbor. All Rights Reserved Privacy policy</div>
</footer>

</body>
</html>
```